Stationary pack for BrightVane

BrightVane is a recently establish Solar brokerage company based in Australia. We have a number of sales staff who provide advice and guidance to both residential and commercial customers regarding solar systems (solar hot water and solar panels.)

In addition to our brokerage services we are also developing software for the solar industry, which will be used to automate the solar system install process. This system will be used by other companies in the solar industry including installers, wholesalers and government departments.

We are after a stationary pack that consists of the following: Business cards, compliments slip and letter head.

The EPS, AI, PNG etc files for the logo are attached.

For the business card:
The name and logo of the company need to be clearly visible. On the back of the business cards, we would like the logo. I am happy for you to split the image part of the logo from the text if you think it would look better a different way.

I would like the business cards to be easily readable with the following information on the front:
Name
(Please leave room for titles for the future – eg Sales Advisor.)
Mobile
Office
Email
Address
ABN

Letter heads:
I would prefer the address to be at the top

Compliments slips:
Only need to be one sided

Target Market(s)

BrightVane provides services to both residential and commercial customers. Our customers will be environmentally conscious.

Industry/Entity Type

Residential

Requirements
Must have
• Business cards must have the logo on the back.

```html
<!DOCTYPE html>
<html lang="en">
<head>
<meta charset="utf-8">
<title>BrightVane – Compliments Slip</title>
<link rel="stylesheet" href="https://fonts.googleapis.com/css2?family=Arimo:wght@700&family=Inconsolata:wght@400&display=swap">
<style>
  :root {
    --backdrop: #dcdcdc;
    --paper: #ffffff;
    --brand-green: #5fa12f;
    --brand-blue: #1d4f91;
    --contact-grey: #a9a9a9;
    --panel-tint: #e6efdc;
    --panel-fade: #f4f8ef;
  }
  * { margin: 0; padding: 0; box-sizing: border-box; }
  html, body {
    width: 1200px;
    height: 900px;
    overflow: hidden;
    background: var(--backdrop);
  }
  .compliments-slip {
    position: absolute;
    left: 60px;
    top: 160px;
    width: 1080px;
    height: 546px;
    background: var(--paper);
    overflow: hidden;
  }
  .panel-sweep {
    position: absolute;
    inset: 0;
    width: 1080px;
    height: 546px;
  }
  .brand {
    position: absolute;
    left: 70px;
    top: 44px;
  }
  .brand-dot {
    display: block;
    width: 84px;
    height: 84px;
    margin-left: 42px;
    border-radius: 50%;
    background: var(--brand-green);
  }
  .brand-name {
    display: block;
    margin-top: 12px;
    font-family: "Arimo", Arial, sans-serif;
    font-weight: 700;
    font-size: 40px;
    letter-spacing: -1px;
    color: var(--brand-green);
    line-height: 1;
  }
  .contact {
    position: absolute;
    left: 70px;
    top: 194px;
    font-family: "Inconsolata", "Courier New", monospace;
    font-size: 15px;
    line-height: 24px;
    color: var(--contact-grey);
    font-style: normal;
  }
  .contact p + p { margin-top: 18px; }
  .slip-title {
    position: absolute;
    left: 72px;
    top: 444px;
    font-family: "Arimo", Arial, sans-serif;
    font-weight: 700;
    font-size: 18px;
    letter-spacing: -0.6px;
    color: var(--brand-blue);
  }
</style>
</head>
<body>
  <section class="compliments-slip">
    <svg class="panel-sweep" viewBox="0 0 1080 546" role="img" aria-label="Faint solar panel array sweeping across the slip">
      <defs>
        <linearGradient id="panelGlow" x1="0" y1="0" x2="1" y2="1">
          <stop offset="0" stop-color="var(--panel-tint)"/>
          <stop offset="1" stop-color="var(--panel-fade)"/>
        </linearGradient>
      </defs>
      <path d="M0,0 L280,0 Q520,380 940,546 L600,546 Q250,470 0,360 Z" fill="url(#panelGlow)"/>
    </svg>

    <div class="brand">
      <span class="brand-dot"></span>
      <span class="brand-name">brightvane</span>
    </div>

    <address class="contact">
      <p>48 sunray road<br>Town, postcode</p>
      <p>T: 01632 960 418</p>
      <p>info@brightvane.com<br>www.brightvane.com</p>
    </address>

    <h1 class="slip-title">WITH COMPLIMENTS</h1>
  </section>
</body>
</html>
```